TrelWave Agile Coaching Website

I need an updated website for www.trelwave-demo.com. I'm looking for a modern look. This is a professional site, but I don't want it to look "stuffy". It needs to have an element of fun and learning.

My services include:
Lean Agile Coaching
Lean Agile Training
Facilitation
Workshops
Consulting

Ideas this site should convey: collaboration, learning, teamwork, adaptability, flow, limited WIP, agility, Lean.

I would like to use some of my own photos and slide decks for content: http://www.deckshelf-example.net/mirabrecken/presentations

I would also like to include the WorkWeb recommendations I have from customers: https://www.workweb-example.com/in/mirabrecken

Examples of sites I like:
http://www.corvalpine-example.com
http://www.stridemoss-example.com

Target Market(s)

IT professionals, software development managers

Industry/Entity Type

It Company

Coding

Coded - Design and coding required

Font styles to use
Serif
Sans Serif

Requirements
Must have
• Original looking graphics and layout.
• My logo must be included in layout.
• Need to feature my blog content.
• Deliverable must be a WordPress theme that I can install.
• Responsive site.
Nice to have
• Use images from my slides on DeckShelf if they make sense.

```html
<!DOCTYPE html>
<html lang="en">
<head>
<meta charset="utf-8">
<title>TrelWave — Agile Coaching</title>
<link href="https://fonts.googleapis.com/css2?family=Raleway:wght@400;500;600;700&display=swap" rel="stylesheet">
<style>
:root{
  --green:#0ccc3a;
  --ink:#1c1c1c;
  --text:#8a8a8a;
  --grey-band:#e2e2e2;
  --grey-soft:#efefef;
  --dark:#2a2a2a;
  --white:#ffffff;
}
*{box-sizing:border-box;margin:0;padding:0}
html,body{width:1200px;height:2903px;overflow:hidden}
body{font-family:'Raleway',sans-serif;color:var(--ink);background:var(--white);position:relative}
.abs{position:absolute}
.btn{position:absolute;background:var(--green);color:var(--white);font-size:11px;font-weight:600;text-transform:uppercase;display:flex;align-items:center;justify-content:center;border-radius:2px;letter-spacing:.3px}
.btn.dark{background:var(--dark)}
.heading{position:absolute;left:184px;font-size:25px;font-weight:700;line-height:29px;text-transform:uppercase}
.heading span{display:block;color:var(--green)}
.body-text{font-size:12.5px;line-height:16.5px;color:var(--text)}

/* header */
.site-header{position:absolute;left:0;top:0;width:1200px;height:81px;background:var(--white)}
.brand{position:absolute;left:184px;top:14px;display:flex;align-items:center;gap:10px;font-size:40px;font-weight:700;letter-spacing:-1px;color:var(--ink)}
.brand i{width:14px;height:34px;background:var(--green);display:block}
.main-nav{position:absolute;left:645px;top:30px;display:flex;gap:26px;font-size:12px;font-weight:700;text-transform:uppercase}
.main-nav a{color:var(--ink);text-decoration:none;padding-bottom:8px}
.main-nav a.current{color:var(--green);border-bottom:2px solid var(--green)}
.search{position:absolute;left:1002px;top:29px}

/* hero */
.hero{position:absolute;left:0;top:81px;width:1200px;height:463px;background:linear-gradient(100deg,#3a3633 0%,#5a524c 35%,#4a4440 60%,#2e2b29 100%)}
.hero-quote{position:absolute;left:184px;top:86px;font-size:34px;line-height:47px;font-weight:700;color:var(--white);text-transform:uppercase}
.hero-rule{position:absolute;left:184px;top:231px;width:24px;height:2px;background:var(--white)}
.hero-sub{position:absolute;left:226px;top:222px;font-size:14px;line-height:25px;color:var(--white)}

/* about */
.about-frame{position:absolute;left:184px;top:625px;width:286px;height:346px;border:12px solid #ececec}
.about-photo{position:absolute;left:213px;top:596px;width:286px;height:344px;background:linear-gradient(90deg,#d7d3cb 0%,#c9c3b8 40%,#2e3447 60%,#1f2638 100%);border-radius:3px}
.about-title{position:absolute;left:551px;top:680px;font-size:27px;font-weight:700}
.about-title b{color:var(--green)}
.about-rule{position:absolute;left:551px;top:736px;width:24px;height:2px;background:var(--ink)}
.about-text{position:absolute;left:591px;top:729px;width:340px}

/* services */
.services{position:absolute;left:0;top:1016px;width:1200px;height:321px;background:var(--grey-band)}
.service{position:absolute;top:101px;width:186px}
.service svg{display:block;height:48px}
.service h3{font-size:12px;font-weight:600;text-transform:uppercase;margin-top:22px}
.service p{margin-top:12px}
.service .btn{position:static;width:89px;height:31px;margin-top:20px}

/* approach */
.card{position:absolute;top:1461px;width:263px}
.card .img{height:182px}
.card h3{font-size:12px;font-weight:600;text-transform:uppercase;margin-top:24px}
.card p{margin-top:10px}
.card p b{color:var(--ink);font-weight:600}
.more{display:block;margin-top:12px;font-size:11px;font-weight:600;color:var(--green)}

/* blog */
.blog{position:absolute;left:0;top:1811px;width:1200px;height:571px;background:var(--grey-soft)}
.post{position:absolute;top:109px;width:263px}
.post .img{height:218px;position:relative}
.date{position:absolute;left:10px;top:14px;width:46px;height:68px;background:rgba(235,235,235,.9);text-align:center;padding-top:10px}
.date b{display:block;font-size:24px;font-weight:500;color:var(--ink)}
.date small{font-size:9px;color:var(--text);text-transform:uppercase}
.post h3{display:flex;align-items:center;gap:15px;font-size:12px;font-weight:600;text-transform:uppercase;margin-top:25px}
.post h3 i{width:27px;height:27px;background:var(--green);border-radius:3px;display:flex;align-items:center;justify-content:center}
.post p,.post .more{margin-left:37px}
.post p{margin-top:18px}

/* cta */
.cta{position:absolute;left:0;top:2382px;width:1200px;height:114px;background:var(--dark);overflow:hidden}
.cta-text{position:absolute;left:184px;top:38px;font-size:12px;line-height:20px;font-weight:700;color:var(--white);text-transform:uppercase}

/* contact */
.newsletter{position:absolute;left:0;top:2539px;width:600px;height:298px;background:var(--green)}
.newsletter h2{position:absolute;left:232px;top:26px;font-size:25px;font-weight:500;color:var(--white);text-transform:uppercase}
.field{position:absolute;left:232px;width:308px;height:33px;background:var(--grey-soft);font-size:10px;color:#777;padding:11px 10px}
.contact{position:absolute;left:600px;top:2539px;width:600px;height:298px;background:#ececec}
.contact .brand{left:58px;top:28px;font-size:48px}
.contact .brand i{height:42px}
.line{position:absolute;left:58px;display:flex;align-items:center;gap:14px;font-size:12px;color:#555}
.line .dot{width:36px;height:36px;border:1px solid #999;border-radius:50%;display:flex;align-items:center;justify-content:center;flex:none}
.line b{color:var(--green);font-weight:600}
.site-footer{position:absolute;left:0;top:2837px;width:1200px;height:66px;background:var(--dark)}
.site-footer p{position:absolute;left:184px;top:26px;font-size:11px;color:#ddd}
.social{position:absolute;top:15px;width:36px;height:36px;border:1px solid #ccc;border-radius:50%}
</style>
</head>
<body>

<header class="site-header">
  <div class="brand"><i></i>TrelWave</div>
  <nav class="main-nav">
    <a class="current" href="#">Home</a><a href="#">About</a><a href="#">Contact</a><a href="#">Service</a>
  </nav>
  <svg class="search" width="14" height="14" viewBox="0 0 14 14"><circle cx="5.5" cy="5.5" r="4" fill="none" stroke="#1c1c1c" stroke-width="2"/><line x1="8.5" y1="8.5" x2="13" y2="13" stroke="#1c1c1c" stroke-width="2"/></svg>
</header>

<section class="hero" role="img" aria-label="Team gathered around a table working with sticky notes">
  <h1 class="hero-quote">"Clarity, Understanding,<br>Improvement"</h1>
  <div class="hero-rule"></div>
  <p class="hero-sub">Improving Software Development Through Alignment<br>Visibility, Knowledge, And Discipline</p>
  <div class="btn" style="left:184px;top:325px;width:156px;height:45px">Explore More</div>
</section>

<section class="about">
  <div class="about-frame"></div>
  <div class="about-photo" role="img" aria-label="Coach presenting in front of a projected slide"></div>
  <h2 class="about-title"><b>ABOUT</b> US</h2>
  <div class="about-rule"></div>
  <p class="about-text body-text">TrelWave is a company dedicated to improving the art and science of software development for both the consumers of software services and the professionals doing the work. Our primary focus is the marketplace...</p>
  <div class="btn" style="left:551px;top:820px;width:89px;height:31px">Read More</div>
</section>

<section class="services">
  <h2 class="heading" style="top:28px">Our<span>Services</span></h2>
  <div class="service" style="left:190px">
    <svg width="48" height="48" viewBox="0 0 48 48" fill="none" stroke="#1c1c1c" stroke-width="2"><path d="M6 20c0-8 8-13 17-13s17 5 17 13-8 13-17 13c-3 0-5 0-7-1l-8 5 2-7c-3-2-4-6-4-10z"/><path d="M16 37c3 3 7 4 12 4 2 0 4 0 5-1l7 4-1-6"/></svg>
    <h3>Consulting</h3>
    <p class="body-text">lorem ipsum' will uncover many web sites still in their infancy. Various versions have...</p>
    <div class="btn">Read More</div>
  </div>
  <div class="service" style="left:404px">
    <svg width="48" height="48" viewBox="0 0 48 48" fill="none" stroke="#1c1c1c" stroke-width="2"><path d="M6 18h8l20-10v30L14 28H6z"/><path d="M10 28l4 12h6l-3-12"/><path d="M38 18c3 1 3 7 0 8"/></svg>
    <h3>Coaching</h3>
    <p class="body-text">lorem ipsum' will uncover many web sites still in their infancy. Various versions have...</p>
    <div class="btn">Read More</div>
  </div>
  <div class="service" style="left:619px">
    <svg width="48" height="48" viewBox="0 0 48 48" fill="none" stroke="#1c1c1c" stroke-width="2"><path d="M8 40l4-10 26-26 6 6-26 26z"/><path d="M34 8l6 6"/><path d="M40 40L10 10l4-4 30 30z"/><path d="M18 14l3-3M24 20l3-3M30 26l3-3"/></svg>
    <h3>Facilitation</h3>
    <p class="body-text">lorem ipsum' will uncover many web sites still in their infancy. Various versions have...</p>
    <div class="btn">Read More</div>
  </div>
  <div class="service" style="left:834px">
    <svg width="48" height="48" viewBox="0 0 48 48" fill="none" stroke="#1c1c1c" stroke-width="2"><rect x="4" y="4" width="10" height="10"/><rect x="20" y="4" width="10" height="10"/><rect x="34" y="4" width="10" height="10"/><rect x="4" y="20" width="10" height="10"/><rect x="20" y="20" width="10" height="10"/><path d="M14 9h6M30 9h4M9 14v6M25 14v6M25 30v8h-8M9 30v12M34 30l4 12M38 30l-4 12"/></svg>
    <h3>Training</h3>
    <p class="body-text">lorem ipsum' will uncover many web sites still in their infancy. Various versions have...</p>
    <div class="btn">Read More</div>
  </div>
</section>

<section class="approach">
  <h2 class="heading" style="top:1376px">Our<span>Approach</span></h2>
  <article class="card" style="left:184px">
    <div class="img" role="img" aria-label="Reflective metal sculpture in a city plaza" style="background:linear-gradient(180deg,#c9cdd2 0%,#9aa0a6 55%,#6b6e70 100%)"></div>
    <h3>Clarity</h3>
    <p class="body-text">Knowledge work endeavors such as software development projects seem anything but clear when in process...</p>
    <span class="more">Read More &raquo;</span>
  </article>
  <article class="card" style="left:468px">
    <div class="img" role="img" aria-label="Workshop participants writing on sticky notes" style="background:linear-gradient(135deg,#4a4340 0%,#8e8279 50%,#c9bfb6 100%)"></div>
    <h3>Understanding</h3>
    <p class="body-text">Regardless if you are new to Agile and Lean, or your organization is now doing Agile, a better understanding of the...</p>
    <span class="more">Read More &raquo;</span>
  </article>
  <article class="card" style="left:753px">
    <div class="img" role="img" aria-label="Kanban board on a wall covered in sticky notes" style="background:linear-gradient(180deg,#ddd8cc 0%,#d8d0b6 50%,#b8ae98 100%)"></div>
    <h3>Improvement</h3>
    <p class="body-text"><b>Agile is not a Destination!</b><br>It is sometimes hard to tell from the predominant Agile literature...</p>
    <span class="more">Read More &raquo;</span>
  </article>
</section>

<section class="blog">
  <h2 class="heading" style="top:39px">Our<span>Latest Blog</span></h2>
  <article class="post" style="left:184px">
    <div class="img" role="img" aria-label="Business team gathered around a laptop" style="background:linear-gradient(135deg,#e8e8e8 0%,#8a8a8a 45%,#2a2a2e 100%)"><div class="date"><b>21</b><small>May</small></div></div>
    <h3><i><svg width="13" height="13" viewBox="0 0 13 13" fill="none" stroke="#fff" stroke-width="2"><path d="M5 8l3-3M4 6L2 8a2 2 0 003 3l2-2M9 7l2-2a2 2 0 00-3-3L6 4"/></svg></i>Speaking at FlowSummit 2016</h3>
    <p class="body-text">I'm pleased to announce I'll be speaking at FlowSummit 2016. My topic will be Minimal Viable Agile...</p>
    <span class="more">Read More &raquo;</span>
  </article>
  <article class="post" style="left:468px">
    <div class="img" role="img" aria-label="Two colleagues reviewing a tablet together" style="background:linear-gradient(135deg,#f0f0f0 0%,#9c9c9c 45%,#2c2c30 100%)"><div class="date"><b>15</b><small>May</small></div></div>
    <h3><i><svg width="13" height="13" viewBox="0 0 13 13" fill="none" stroke="#fff" stroke-width="2"><path d="M5 8l3-3M4 6L2 8a2 2 0 003 3l2-2M9 7l2-2a2 2 0 00-3-3L6 4"/></svg></i>Lean Flow Riverton Conference</h3>
    <p class="body-text">Join us for Riverton's first Lean Flow conference. We have a great lineup of speakers. And if the lecture...</p>
    <span class="more">Read More &raquo;</span>
  </article>
  <article class="post" style="left:753px">
    <div class="img" role="img" aria-label="Meeting around a conference table" style="background:linear-gradient(135deg,#d8dcd2 0%,#8e8f86 45%,#3a3a3c 100%)"><div class="date"><b>04</b><small>May</small></div></div>
    <h3><i><svg width="13" height="13" viewBox="0 0 13 13" fill="none" stroke="#fff" stroke-width="2"><path d="M5 8l3-3M4 6L2 8a2 2 0 003 3l2-2M9 7l2-2a2 2 0 00-3-3L6 4"/></svg></i>Speaking at RDC</h3>
    <p class="body-text">I will be participating in, and speaking at the 2014 Riverton Developer's Conference May 15, 16, 17...</p>
    <span class="more">Read More &raquo;</span>
  </article>
  <div class="btn" style="left:522px;top:503px;width:155px;height:37px">View All Blog</div>
</section>

<section class="cta">
  <svg class="abs" style="left:0;top:0" width="1200" height="114"><polygon points="681,0 1200,0 1200,114 755,114" fill="#0ccc3a"/></svg>
  <p class="cta-text">Typesheet sheets containing lorem ipsum passages, and<br>recently with desktop publishing software like.</p>
  <div class="btn dark" style="left:807px;top:37px;width:157px;height:38px">Explore PPT</div>
</section>

<section class="newsletter">
  <h2>Newsletter Sign Up</h2>
  <div class="field" style="top:83px">Your Name</div>
  <div class="field" style="top:131px">Your Email</div>
  <div class="btn dark" style="left:232px;top:176px;width:116px;height:35px;text-transform:none;font-size:11px">Send &#10148;</div>
</section>

<section class="contact">
  <div class="brand"><i></i>TrelWave</div>
  <div class="line" style="top:108px"><span class="dot"><svg width="12" height="16" viewBox="0 0 12 16"><path d="M6 1a5 5 0 00-5 5c0 4 5 9 5 9s5-5 5-9a5 5 0 00-5-5z" fill="none" stroke="#333" stroke-width="1.6"/><circle cx="6" cy="6" r="1.8" fill="#333"/></svg></span><span><b>Address:</b> 198 men who are so beguiled and<br>demoralized 1234</span></div>
  <div class="line" style="top:160px"><span class="dot"><svg width="14" height="14" viewBox="0 0 14 14"><path d="M3 1l3 3-2 2c1 2 2 3 4 4l2-2 3 3-2 2C6 13 1 8 1 3z" fill="#333"/></svg></span><span><b>Phone:</b> <span style="font-size:17px;color:#555">123-456-7890</span></span></div>
  <div class="line" style="top:214px"><span class="dot"><svg width="14" height="10" viewBox="0 0 14 10"><rect x="0.8" y="0.8" width="12.4" height="8.4" fill="none" stroke="#333" stroke-width="1.4"/><path d="M1 1l6 5 6-5" fill="none" stroke="#333" stroke-width="1.4"/></svg></span><span><b>Email:</b> <u>info@trelwave-demo.com</u></span></div>
</section>

<footer class="site-footer">
  <p>Copyright &copy; 2016 trelwave-demo.com</p>
  <span class="social" style="left:917px"></span>
  <span class="social" style="left:979px"></span>
</footer>

</body>
</html>
```